Veloria Energy (Alternative Energy)

We sell solar panels and geothermal heating and cooling applications.
We want to emphasize that we can offer AFFORDABLE solar and thermal heating applications.
Governmental 30% tax rebate if ordered by 2017.
Solar panels from 40 -90% efficient
Units pay for themselves
Can be used with current (existing) water and heating systems
Lower energy consumption
Great Backup Heaters in case of power outage.
100% solar powered units. Self running thermosphyin design
Low maintenance
Can be Self installed
Saves the environment
Zero Emissions
Increases homes resale value
Great for remote locations
Increases Jobs

Target Market(s)

V.E.

Industry/Entity Type

Solar

Logo Text

The future is here

Number of Pages Required

5+ page

Font styles to use
Serif

Colors
f37122
fbee3e
acd036
ffffff
000000

Requirements
Must have
• Emphasize that we can offer affordable solar and thermal heating applications
• Pays for themselves within 1-3 years
• Solar panels from 40 -90% efficient
• 100% sustainable and renewable
• Very little sun light required
Nice to have
• Very professional clean modern web design
• Needs to achieve sales results.
Should not have
• any lingo. or confusion. Must be simple and effective. Needs to achieve sales results.

```html
<!DOCTYPE html>
<html lang="en">
<head>
<meta charset="utf-8">
<title>Veloria Energy</title>
<link href="https://fonts.googleapis.com/css2?family=Open+Sans:wght@400;600;700&display=swap" rel="stylesheet">
<style>
:root{
  --orange:#f37122;--yellow:#fbee3e;--green:#acd036;--blue:#2b8fd0;
  --teal:#2d7fa3;--navy:#1e5f86;--dark:#222;--darker:#1a1a1a;--grey:#666;--light:#eee;--white:#fff;
}
*{margin:0;padding:0;box-sizing:border-box}
html,body{width:1200px;height:2924px;overflow:hidden;background:var(--white);font-family:"Open Sans",Arial,sans-serif;color:#333}
.site-header{height:100px;display:flex;align-items:center;justify-content:space-between;padding:0 60px;background:var(--white);position:relative;z-index:2}
.brand{font-size:30px;font-weight:600;color:var(--orange)}
.main-nav{display:flex;gap:6px;position:relative}
.main-nav a{font-size:17px;color:#444;padding:10px 16px;text-decoration:none;border-radius:3px}
.main-nav a.current{color:var(--orange)}
.main-nav a.active{background:var(--orange);color:var(--white)}
.dropdown{position:absolute;top:50px;left:146px;width:150px;background:#2f3b45;padding:6px 0}
.dropdown span{display:block;font-size:13px;color:#ccd;padding:9px 14px;border-bottom:1px solid #3e4c57}
.hero{height:500px;background:linear-gradient(180deg,#4f9fdc 0%,#a9d3ef 45%,#9cbf52 70%,#4a6a8a 100%);display:flex;align-items:center;justify-content:center;margin-top:-100px;padding-top:100px}
.hero h1{color:var(--white);font-size:44px;font-weight:600;text-shadow:0 2px 6px rgba(0,0,0,.45)}
.welcome{height:300px;text-align:center;padding:50px 190px 0}
.section-title{font-size:34px;font-weight:400;color:#333;margin-bottom:26px}
.welcome p{font-size:15px;line-height:26px;color:var(--grey);margin-bottom:14px}
.optimize{height:300px;background:var(--teal);text-align:center;padding-top:34px}
.optimize .section-title{color:var(--white);margin-bottom:20px}
.stats{display:flex;justify-content:space-around;padding:0 80px}
.stat{width:180px;color:var(--white);font-size:15px}
.stat svg{display:block;margin:0 auto 8px}
.offer{height:600px;text-align:center;padding-top:40px}
.offer-grid{display:grid;grid-template-columns:repeat(3,1fr);column-gap:40px;row-gap:34px;padding:0 140px}
.offer-item h3{font-size:17px;font-weight:600;color:#333;margin:12px 0 8px}
.offer-item p{font-size:13px;line-height:20px;color:var(--grey);padding:0 30px}
.offer-icon{width:120px;height:120px;border-radius:50%;background:var(--light);margin:0 auto;display:flex;align-items:center;justify-content:center}
.projects{height:440px;background:var(--navy);text-align:center;padding-top:44px}
.projects .section-title{color:var(--white);margin-bottom:36px}
.carousel{position:relative;display:flex;justify-content:center;gap:8px;padding:0 60px}
.project-shot{width:222px;height:170px}
.arrow{position:absolute;top:66px;width:34px;height:38px;background:rgba(255,255,255,.85);display:flex;align-items:center;justify-content:center}
.arrow.prev{left:50px}.arrow.next{right:50px}
.team{height:420px;text-align:center;padding-top:40px}
.team-row{display:flex;justify-content:center;gap:46px;position:relative}
.member{width:200px}
.member .photo{height:200px;border:4px solid var(--light)}
.member h4{font-size:14px;font-weight:600;color:#444;margin-top:10px;text-transform:uppercase}
.member.featured h4{color:var(--orange)}
.team .round{position:absolute;top:80px;width:44px;height:44px;border-radius:50%;background:#444;display:flex;align-items:center;justify-content:center}
.round.prev{left:110px}.round.next{right:110px}
.site-footer{height:264px;background:var(--dark);color:#bbb;border-top:6px solid var(--orange)}
.footer-cols{display:grid;grid-template-columns:repeat(4,1fr);padding:34px 60px 0;height:204px}
.footer-cols h5{font-size:16px;color:var(--white);font-weight:600;margin-bottom:12px}
.footer-cols li{list-style:none;font-size:13px;line-height:22px}
.footer-cols li::before{content:"› ";color:var(--orange)}
.contact-line{font-size:13px;line-height:20px;display:flex;gap:10px;align-items:flex-start;margin-bottom:10px}
.dot{width:22px;height:22px;border-radius:50%;background:var(--orange);flex:none}
.field{width:200px;height:26px;background:var(--white);margin-bottom:8px;font-size:12px;color:#999;padding:5px 8px}
.submit{display:inline-block;background:var(--orange);color:var(--white);font-size:12px;padding:5px 16px}
.footer-bottom{height:54px;background:var(--darker);display:flex;align-items:center;justify-content:space-between;padding:0 60px;font-size:13px}
.socials{display:flex;gap:8px}
.socials span{width:26px;height:26px;border-radius:50%;background:#555}
</style>
</head>
<body>
<header class="site-header">
  <div class="brand">Veloria Energy</div>
  <nav class="main-nav">
    <a class="current">Home</a><a>About</a><a class="active">Services</a><a>Project</a><a>Testimonial</a><a>Contact Us</a>
    <div class="dropdown"><span>Solar Panel Offer</span><span>Thermal Heat Offer</span><span>Backup Heater Offer</span><span>Home Install Offer</span></div>
  </nav>
</header>

<section class="hero" role="img" aria-label="Wind turbines above a field of solar panels under a blue sky">
  <h1>Saving Money, Saving Energy &amp; Saving the Planet</h1>
</section>

<section class="welcome">
  <h2 class="section-title">Welcome to Veloria Energy</h2>
  <p>We bring affordable solar and thermal heating to every home. Our panels run from 40% to 90% efficient and pay for themselves within one to three years. They work with your existing water and heating systems, need very little sunlight and almost no upkeep.</p>
  <p>Every unit is 100% solar powered, sustainable and renewable. Cut your energy bills, add value to your home and keep warm even during a power outage with our reliable backup heaters.</p>
</section>

<section class="optimize">
  <h2 class="section-title">You Can Optimize:</h2>
  <div class="stats">
    <div class="stat"><svg width="110" height="110" viewBox="0 0 110 110"><circle cx="55" cy="55" r="44" fill="none" stroke="#fff" stroke-width="16"/><circle cx="55" cy="55" r="44" fill="none" stroke="var(--blue)" stroke-width="16" stroke-dasharray="83 276" transform="rotate(-90 55 55)"/><text x="55" y="61" text-anchor="middle" fill="#fff" font-size="17" font-family="Open Sans, sans-serif">30%</text></svg>Tax Rebate</div>
    <div class="stat"><svg width="110" height="110" viewBox="0 0 110 110"><circle cx="55" cy="55" r="44" fill="none" stroke="#fff" stroke-width="16"/><circle cx="55" cy="55" r="44" fill="none" stroke="var(--orange)" stroke-width="16" stroke-dasharray="248 276" transform="rotate(-90 55 55)"/><text x="55" y="61" text-anchor="middle" fill="#fff" font-size="14" font-family="Open Sans, sans-serif">40%-90%</text></svg>Efficient<br>Solar Panels</div>
    <div class="stat"><svg width="110" height="110" viewBox="0 0 110 110"><circle cx="55" cy="55" r="44" fill="none" stroke="var(--green)" stroke-width="16"/><text x="55" y="61" text-anchor="middle" fill="#fff" font-size="17" font-family="Open Sans, sans-serif">100%</text></svg>Solar Powered<br>Units</div>
    <div class="stat"><svg width="110" height="110" viewBox="0 0 110 110"><circle cx="55" cy="55" r="44" fill="none" stroke="#fff" stroke-width="16"/><circle cx="55" cy="55" r="44" fill="none" stroke="var(--yellow)" stroke-width="16" stroke-dasharray="248 276" transform="rotate(-90 55 55)"/><text x="55" y="61" text-anchor="middle" fill="#fff" font-size="17" font-family="Open Sans, sans-serif">90%</text></svg>Time</div>
  </div>
</section>

<section class="offer">
  <h2 class="section-title">What We Offer</h2>
  <div class="offer-grid">
    <div class="offer-item"><div class="offer-icon"><svg width="60" height="60" viewBox="0 0 60 60"><circle cx="30" cy="30" r="28" fill="var(--orange)"/><path d="M30 30 L30 10 M30 30 L13 40 M30 30 L47 40" stroke="#fff" stroke-width="4" stroke-linecap="round"/><path d="M30 30 V52" stroke="#fff" stroke-width="3"/></svg></div><h3>Affordable solar</h3><p>Solar and thermal heating priced for every home, paid back in one to three years.</p></div>
    <div class="offer-item"><div class="offer-icon"><svg width="60" height="60" viewBox="0 0 60 60"><circle cx="30" cy="32" r="20" fill="none" stroke="var(--orange)" stroke-width="5" stroke-dasharray="100 26" transform="rotate(-70 30 32)"/><path d="M30 6 V30" stroke="var(--orange)" stroke-width="5" stroke-linecap="round"/></svg></div><h3>Lower energy</h3><p>Cut your monthly usage while keeping your existing water and heating systems.</p></div>
    <div class="offer-item"><div class="offer-icon"><svg width="60" height="60" viewBox="0 0 60 60"><path d="M14 34 a12 12 0 0 1 6-22 a15 15 0 0 1 26 6 a9 9 0 0 1 0 16 Z" fill="var(--orange)"/><path d="M22 40 l-3 10 M32 40 l-3 10 M42 40 l-3 10" stroke="var(--orange)" stroke-width="3"/></svg></div><h3>Rainwater Harvesting</h3><p>Collect and reuse rainwater with simple add-ons built for lasting savings.</p></div>
    <div class="offer-item"><div class="offer-icon"><svg width="60" height="60" viewBox="0 0 60 60"><path d="M30 10 C16 16 18 30 30 32 C42 30 44 16 30 10Z" fill="var(--orange)"/><path d="M30 32 V42 M8 46 h18 l6 -4 h20 v8 H8Z" stroke="var(--orange)" stroke-width="3" fill="var(--orange)"/></svg></div><h3>Saves the environment</h3><p>Clean, renewable power that protects the planet for the next generation.</p></div>
    <div class="offer-item"><div class="offer-icon"><svg width="60" height="60" viewBox="0 0 60 60"><path d="M8 30 L30 10 L52 30 H46 V52 H14 V30Z" fill="var(--orange)"/><path d="M31 24 l-7 12 h6 l-2 10 l8 -13 h-6z" fill="#fff"/></svg></div><h3>Home Energy Saving</h3><p>Raise your home's resale value while your heating costs keep going down.</p></div>
    <div class="offer-item"><div class="offer-icon"><svg width="60" height="60" viewBox="0 0 60 60"><rect x="17" y="12" width="26" height="40" rx="4" fill="var(--orange)"/><rect x="24" y="7" width="12" height="6" fill="var(--orange)"/><path d="M32 20 l-7 12 h6 l-2 10 l8 -13 h-6z" fill="#fff"/></svg></div><h3>Zero Emissions</h3><p>Fully solar powered units with a self running design and no harmful output.</p></div>
  </div>
</section>

<section class="projects">
  <h2 class="section-title">Our Project</h2>
  <div class="carousel">
    <div class="project-shot" role="img" aria-label="Solar panels on a roof at sunset" style="background:linear-gradient(160deg,#e8a45a,#8a5a3a)"></div>
    <div class="project-shot" role="img" aria-label="Installer fitting rooftop solar panels" style="background:linear-gradient(160deg,#a9c6dc,#4b6f8c)"></div>
    <div class="project-shot" role="img" aria-label="Rows of solar panels on a field" style="background:linear-gradient(160deg,#9fc7e6,#3d5f85)"></div>
    <div class="project-shot" role="img" aria-label="Worker in a hard hat on a solar roof" style="background:linear-gradient(160deg,#b8d46a,#5c7a3a)"></div>
    <div class="project-shot" role="img" aria-label="Solar array under a clear sky" style="background:linear-gradient(160deg,#d7e6f2,#6f8aa3)"></div>
    <div class="arrow prev"><svg width="14" height="18"><path d="M11 2 L3 9 L11 16" fill="none" stroke="#333" stroke-width="3"/></svg></div>
    <div class="arrow next"><svg width="14" height="18"><path d="M3 2 L11 9 L3 16" fill="none" stroke="#333" stroke-width="3"/></svg></div>
  </div>
</section>

<section class="team">
  <h2 class="section-title">Meet Our Team</h2>
  <div class="team-row">
    <div class="member featured"><div class="photo" role="img" aria-label="Team member in a yellow hard hat" style="background:linear-gradient(160deg,#9ec9ea,#e0b84a)"></div><h4>Dana Hollis</h4></div>
    <div class="member"><div class="photo" role="img" aria-label="Engineer beside solar panels" style="background:linear-gradient(160deg,#b7d2e8,#4e6c8a)"></div><h4>Dana Hollis</h4></div>
    <div class="member"><div class="photo" role="img" aria-label="Technician standing by a solar array" style="background:linear-gradient(160deg,#7fb3e0,#2f5878)"></div><h4>Sam Porter</h4></div>
    <div class="member"><div class="photo" role="img" aria-label="Installer working on a rooftop panel" style="background:linear-gradient(160deg,#a8c8e6,#5a6f86)"></div><h4>Rory Quinn</h4></div>
    <div class="round prev"><svg width="14" height="18"><path d="M11 2 L3 9 L11 16" fill="none" stroke="#fff" stroke-width="3"/></svg></div>
    <div class="round next"><svg width="14" height="18"><path d="M3 2 L11 9 L3 16" fill="none" stroke="#fff" stroke-width="3"/></svg></div>
  </div>
</section>

<footer class="site-footer">
  <div class="footer-cols">
    <div><h5>Main menu</h5><ul><li>Home</li><li>About Us</li><li>Service</li><li>Project</li><li>Gallery</li></ul></div>
    <div><h5>Information</h5><ul><li>Partners</li><li>Legal Notes</li><li>Terms and conditions of use</li><li>Benefits of Installation</li><li>Sitemap</li></ul></div>
    <div><h5>Contact us</h5>
      <div class="contact-line"><span class="dot"></span><span>412 Cedar Grove Road<br>Westfield, ON 10230</span></div>
      <div class="contact-line"><span class="dot"></span><span>(555) 014-2290</span></div>
      <div class="contact-line"><span class="dot"></span><span>hello@veloriaenergy.com</span></div>
    </div>
    <div><h5>Quick Contact</h5><p style="font-size:12px;margin-bottom:8px">Send us a quick note</p><div class="field">Your Name</div><div class="field">Email</div><span class="submit">Submit</span></div>
  </div>
  <div class="footer-bottom"><span>&copy;2015 Veloria Energy. All rights reserved.</span><div class="socials"><span></span><span></span><span></span><span></span><span></span><span></span></div></div>
</footer>
</body>
</html>
```